Podcast Cover Art for Inspiring Fun Show

Title: The Dave R Hour

I am looking for a simple design that includes the following:

1. Picture of me (the one I attached with the background removed) on a simple background (please refer to attachments for ideas).
2. The title done in professional lettering that is easy to read and stands out on the background

Please see attached pictures for:

1) Other podcast art I like
2) Backgrounds that I like
3) A picture of me (please edit out the background)

Target Market(s)

Anyone into personal-development, inspiring content and motivational stories.

Font styles to use
Sans Serif

Colors

Designer to choose colors to be used in the design.

Requirements
Must have
• - Title "The Dave R Hour" in professional lettering that is large and very easy to read
• - Picture of me on the background

```html
<!DOCTYPE html>
<html lang="en">
<head>
<meta charset="utf-8">
<title>The Dave R Hour – Podcast Cover</title>
<link rel="stylesheet" href="https://fonts.googleapis.com/css2?family=Montserrat:wght@800;900&display=swap">
<style>
  :root {
    --page: #ececec;
    --purple: #5b1ea0;
    --blue: #2f72d8;
    --green: #2f8d1f;
    --yellow: #f2c400;
    --orange: #f0900f;
    --red: #c5130f;
    --title: #ffffff;
  }
  * { margin: 0; padding: 0; box-sizing: border-box; }
  html, body {
    width: 1200px; height: 1027px; overflow: hidden;
    background: var(--page);
    font-family: "Montserrat", sans-serif;
  }
  .cover {
    position: absolute; left: 120px; top: 33px;
    width: 960px; height: 960px; overflow: hidden;
    box-shadow: 0 6px 24px rgba(0,0,0,.18);
  }
  .bands { position: absolute; inset: 0; }
  .band { height: 160px; position: relative; overflow: hidden; }
  .band--purple { background: linear-gradient(180deg, #4a148a, var(--purple)); }
  .band--blue   { background: linear-gradient(180deg, #1f56b4, var(--blue)); }
  .band--green  { background: linear-gradient(180deg, #226f14, var(--green)); }
  .band--yellow { background: linear-gradient(180deg, #e6b400, var(--yellow)); }
  .band--orange { background: linear-gradient(180deg, #ee9f12, var(--orange)); }
  .band--red    { background: linear-gradient(180deg, #b00e0b, var(--red)); }

  .echo {
    position: absolute;
    font-weight: 800; font-size: 54px; letter-spacing: 1px;
    transform: rotate(-18deg); white-space: nowrap;
    opacity: .45;
  }
  .band--purple .echo { color: #2a0a5e; }
  .band--blue .echo   { color: #122f86; }
  .band--green .echo  { color: #114a08; }
  .band--yellow .echo { color: #2e7a1a; }

  .portrait {
    position: absolute; left: 430px; top: 70px;
    width: 530px; height: 620px;
    border-radius: 46% 46% 8% 30%;
    background: radial-gradient(ellipse at 45% 40%, rgba(245,245,245,.85) 0%, rgba(170,170,170,.75) 45%, rgba(30,30,30,.85) 100%);
    mix-blend-mode: luminosity;
  }

  .title {
    position: absolute; left: 56px; top: 728px;
    color: var(--title);
    font-weight: 900; line-height: .95;
    text-transform: uppercase;
  }
  .title__small { display: block; font-size: 40px; letter-spacing: 8px; margin-bottom: 4px; }
  .title__big   { display: block; font-size: 92px; letter-spacing: 1px; white-space: nowrap; }
</style>
</head>
<body>
  <main class="cover">
    <div class="bands">
      <div class="band band--purple">
        <span class="echo" style="left:-20px; top:70px;">DAVE R</span>
      </div>
      <div class="band band--blue">
        <span class="echo" style="left:60px; top:40px;">DAVE R</span>
      </div>
      <div class="band band--green">
        <span class="echo" style="left:30px; top:50px;">DAVE R</span>
      </div>
      <div class="band band--yellow">
        <span class="echo" style="left:-40px; top:60px;">DAVE R</span>
      </div>
      <div class="band band--orange"></div>
      <div class="band band--red"></div>
    </div>

    <div class="portrait" role="img" aria-label="Cut-out photo of the host smiling, black and white with rainbow tint"></div>

    <h1 class="title">
      <span class="title__small">The</span>
      <span class="title__big">Dave R Hour</span>
    </h1>
  </main>
</body>
</html>
```